Brightwell Homes Guide Business card

I have had at the logo designed here and attached. The business compares off the plan apartments in Sydney and provides quick comparison for new home buyers e.g price, floor plans and location. I would like the complimentary colours used on the business card. I would like it be unique but also look professional. I also have a website to gain inspiration from www.brightwellhomesguide.com.au
Updates
Industry/Entity Type
Business
Contact Information for Business Card
Helen Vostrakis
Director of Business Development
e: helen.vostrakis@brightwellhomesguide.com.au
p: (02) 8143 7692
m: 0431 572 908
w: www.brightwellhomesguide.com.au
Look and feel
Each slider illustrates characteristics of the customer's brand and the style your logo design should communicate.

```html
<!DOCTYPE html>
<html lang="en">
<head>
<meta charset="utf-8">
<title>Brightwell Homes Guide – Business Card</title>
<link rel="stylesheet" href="https://fonts.googleapis.com/css2?family=PT+Sans:wght@400;700&display=swap">
<style>
  :root {
    --stage: #e9e7e3;
    --charcoal: #3b3b3d;
    --charcoal-light: #48484b;
    --paper: #f4f4f4;
    --leaf: #7cc242;
    --sky: #3a8fd1;
    --ink-light: #f2f2f2;
  }
  * { box-sizing: border-box; margin: 0; padding: 0; }
  html, body { width: 1200px; height: 1200px; overflow: hidden; }
  body {
    background: var(--stage);
    font-family: "PT Sans", Arial, sans-serif;
    display: flex;
    flex-direction: column;
    align-items: center;
    justify-content: center;
    gap: 52px;
  }
  .card {
    position: relative;
    width: 900px;
    height: 514px;
    overflow: hidden;
    box-shadow: 0 6px 18px rgba(0,0,0,0.18);
  }

  /* Front */
  .card-front {
    background: linear-gradient(160deg, var(--charcoal-light) 0%, var(--charcoal) 60%, #333335 100%);
  }
  .front-brand {
    position: absolute;
    left: 0; right: 0; top: 200px;
    display: flex;
    align-items: center;
    justify-content: center;
    gap: 22px;
  }
  .brand-mark {
    width: 60px; height: 60px;
    background: var(--sky);
    flex: none;
  }
  .brand-name {
    color: var(--leaf);
    font-weight: 400;
    font-size: 54px;
    line-height: 1;
    letter-spacing: 0.5px;
    white-space: nowrap;
  }
  .front-web {
    position: absolute;
    left: 0; right: 0; bottom: 34px;
    text-align: center;
    color: var(--ink-light);
    font-size: 19px;
    letter-spacing: 0.3px;
  }

  /* Back */
  .card-back { background: var(--paper); }
  .split-band { position: absolute; inset: 0; }
  .back-brand {
    position: absolute;
    left: 48px; top: 52px;
    display: flex;
    align-items: center;
    gap: 12px;
  }
  .back-brand .brand-mark { width: 34px; height: 34px; }
  .back-brand .brand-name { font-size: 30px; }
  .holder {
    position: absolute;
    left: 560px; top: 160px;
  }
  .holder-name {
    color: var(--leaf);
    font-size: 28px;
    line-height: 1.1;
  }
  .holder-title {
    color: var(--ink-light);
    font-size: 19px;
    margin-top: 4px;
  }
  .contact-list {
    position: absolute;
    left: 480px; top: 302px;
    list-style: none;
    color: var(--ink-light);
    font-size: 19px;
  }
  .contact-list li {
    display: flex;
    align-items: center;
    gap: 12px;
    height: 34px;
    white-space: nowrap;
  }
  .contact-icon { width: 20px; height: 20px; flex: none; }
  .social-links {
    position: absolute;
    left: 700px; top: 398px;
    display: flex;
    gap: 10px;
  }
  .social-links span {
    width: 22px; height: 22px;
    border-radius: 4px;
    background: var(--leaf);
  }
</style>
</head>
<body>

  <section class="card card-front" aria-label="Business card front">
    <div class="front-brand">
      <span class="brand-mark"></span>
      <span class="brand-name">Brightwell Homes Guide</span>
    </div>
    <p class="front-web">www.brightwellhomesguide.com.au</p>
  </section>

  <section class="card card-back" aria-label="Business card back">
    <svg class="split-band" viewBox="0 0 900 514" aria-hidden="true">
      <polygon points="200,514 440,120 900,120 900,514" fill="var(--charcoal)"/>
      <line x1="200" y1="514" x2="440" y2="120" stroke="var(--leaf)" stroke-width="16"/>
      <line x1="440" y1="120" x2="900" y2="120" stroke="var(--leaf)" stroke-width="10"/>
    </svg>

    <div class="back-brand">
      <span class="brand-mark"></span>
      <span class="brand-name">Brightwell Homes Guide</span>
    </div>

    <div class="holder">
      <p class="holder-name">Daniel Harcourt</p>
      <p class="holder-title">Managing Partner</p>
    </div>

    <ul class="contact-list">
      <li>
        <svg class="contact-icon" viewBox="0 0 20 20" aria-hidden="true">
          <path d="M3 7c0-2 2-3.5 7-3.5S17 5 17 7v1.5h-3.5V7c-1-.6-6-.6-7 0v1.5H3z" fill="var(--sky)"/>
          <rect x="5" y="10" width="10" height="7" rx="1.5" fill="var(--sky)"/>
        </svg>
        000.000.0000
      </li>
      <li>
        <svg class="contact-icon" viewBox="0 0 20 20" aria-hidden="true">
          <rect x="1" y="4" width="18" height="12" rx="1" fill="var(--sky)"/>
          <polyline points="1.5,4.5 10,11 18.5,4.5" fill="none" stroke="var(--charcoal)" stroke-width="1.5"/>
        </svg>
        dharcourt@brightwellhomesguide.com.au
      </li>
    </ul>

    <div class="social-links" aria-label="Social profiles">
      <span></span>
      <span></span>
    </div>
  </section>

</body>
</html>
```